Plakat-Design für Bauunternehmung
Zielgruppe
Wir sind eine Bauunternehmung (Meisterbetrieb und Ingenieurbüro) welche Erd- Maurer- und Betonarbeiten anbietet. Unser Fokus liegt auf Professionalität und qualitativ einwandfreie Arbeit. Wir sind teuer aber die besten in dem was wir machen. Unsere Zielgruppe liegt bei Kunden welche eine qualitativ einwandfreie Arbeit erwarten und bewusst sind dass das auch Geld kostet. Unserem Kunden ist die Geldfrage immer zweitrangig und er legt viel mehr wert auf andere Faktoren: Qualität, Zuverlässigkeit, Qualifikation, Termineinhaltung etc. Es ist selbstverständlich das die Kunden meist vermögender sind.
Aufgabenstellung
Format: 340 x 175 cm
Was muss drauf:
- Logo
- Firmendaten:
Lindmoosweg 7, 89079 Ulm
Telefon: +49 (0) 7305 - 4418273
Mobil: +49 (0) 176 - 20394857
E-Mail: mortek@beispielpost.de
- Zusätzliche Informationen: Es sollte irgendwo noch 'Bauunternehmung' stehen, es sollte etwas größer sein, unter Logo oder ähnlich, Es muss klar sein das wir eine Bauunternehmung sind. Zusätzlich dazu noch unsere Leistungen 'Neubau, Umbau, Anbau', nebeneinander oder übereinander ist euch überlassen.

```html
<!DOCTYPE html>
<html lang="de">
<head>
<meta charset="utf-8">
<title>mortek Bauunternehmung – Bannerentwürfe</title>
<link href="https://fonts.googleapis.com/css2?family=Poppins:wght@500;600&display=swap" rel="stylesheet">
<style>
  :root {
    --page-bg: #d9d9d9;
    --banner-dark: #2b2c2e;
    --banner-mid: #3a3b3d;
    --ink-light: #f2f2f2;
    --ink-dark: #2a2b2d;
  }
  * { box-sizing: border-box; margin: 0; padding: 0; }
  html, body { width: 857px; height: 1200px; overflow: hidden; }
  body {
    background: var(--page-bg);
    font-family: "Poppins", sans-serif;
    position: relative;
  }
  .banner {
    position: absolute;
    left: 113px;
    width: 652px;
    height: 327px;
    color: var(--ink-light);
    overflow: hidden;
  }
  .banner--de { top: 138px; }
  .banner--en { top: 739px; }
  .banner__backdrop {
    position: absolute; inset: 0;
    background: linear-gradient(115deg, var(--banner-dark) 0%, var(--banner-mid) 35%, var(--banner-dark) 60%, var(--banner-mid) 80%, var(--banner-dark) 100%);
  }
  .brand {
    position: absolute;
    left: 148px; top: 18px;
    display: flex; align-items: flex-end; gap: 20px;
    height: 88px;
  }
  .brand__square {
    width: 87px; height: 88px;
    background: var(--ink-light);
  }
  .brand__block {
    height: 88px;
    display: flex; flex-direction: column; justify-content: space-between;
  }
  .brand__qualifier {
    font-weight: 500; font-size: 10px; line-height: 14px;
    white-space: nowrap;
  }
  .brand__name {
    font-weight: 600; font-size: 52px; line-height: 60px;
  }
  .headline {
    position: absolute; left: 0; right: 0; top: 124px;
    text-align: center;
    font-weight: 600; font-size: 43px; line-height: 54px;
  }
  .services {
    position: absolute; left: 0; right: 0; top: 185px; height: 49px;
    background: var(--ink-light);
    color: var(--ink-dark);
    text-align: center;
    font-weight: 600; font-size: 36px; line-height: 50px;
  }
  .address {
    position: absolute; left: 37px; right: 37px; top: 247px;
    display: flex; align-items: center; gap: 14px;
    font-weight: 600; font-size: 20px; line-height: 26px; white-space: nowrap;
  }
  .address::before, .address::after {
    content: ""; flex: 1; height: 1px; background: var(--ink-light);
  }
  .contacts {
    position: absolute; left: 17px; right: 17px; top: 287px;
    display: flex; justify-content: space-between; align-items: center;
    font-weight: 500; font-size: 14.5px; line-height: 22px; white-space: nowrap;
  }
  .contact { display: flex; align-items: center; gap: 6px; }
  .contact__icon { width: 22px; height: 22px; flex: none; }
</style>
</head>
<body>

<svg width="0" height="0" style="position:absolute" aria-hidden="true">
  <defs>
    <symbol id="icon-phone" viewBox="0 0 22 22">
      <rect width="22" height="22" fill="#f2f2f2"/>
      <path d="M7 5c1 0 2 2.5 2 3s-1 1-1 1.5c.5 1.5 2 3 3.5 3.5.5 0 1-1 1.5-1s3 1 3 2-1.5 2.5-2.5 2.5C9 17 5 13 5 7.5 5 6.5 6 5 7 5z" fill="#2a2b2d"/>
    </symbol>
    <symbol id="icon-mobile" viewBox="0 0 22 22">
      <rect width="22" height="22" fill="#f2f2f2"/>
      <rect x="6.5" y="3.5" width="9" height="15" rx="1.5" fill="#2a2b2d"/>
      <rect x="8" y="5.5" width="6" height="9.5" fill="#f2f2f2"/>
      <circle cx="11" cy="16.7" r="0.9" fill="#f2f2f2"/>
    </symbol>
    <symbol id="icon-mail" viewBox="0 0 22 22">
      <rect width="22" height="22" fill="#f2f2f2"/>
      <rect x="4.5" y="6.5" width="13" height="9" fill="none" stroke="#2a2b2d" stroke-width="1.4"/>
      <path d="M4.5 6.5l6.5 5 6.5-5" fill="none" stroke="#2a2b2d" stroke-width="1.4"/>
    </symbol>
  </defs>
</svg>

<section class="banner banner--de">
  <div class="banner__backdrop" role="img" aria-label="Dunkler Hintergrund mit weichen diagonalen Lichtstreifen"></div>
  <div class="brand">
    <div class="brand__square"></div>
    <div class="brand__block">
      <span class="brand__qualifier">MEISTERBETRIEB &amp; INGENIEURBÜRO</span>
      <span class="brand__name">mortek</span>
    </div>
  </div>
  <h1 class="headline">BAUUNTERNEHMUNG</h1>
  <p class="services">NEUBAU – UMBAU – ANBAU</p>
  <p class="address">Lindmoosweg 7, 89079 Ulm</p>
  <div class="contacts">
    <span class="contact"><svg class="contact__icon"><use href="#icon-phone"/></svg>+49 (0) 7305 - 4418273</span>
    <span class="contact"><svg class="contact__icon"><use href="#icon-mobile"/></svg>+49 (0) 176 - 20394857</span>
    <span class="contact"><svg class="contact__icon"><use href="#icon-mail"/></svg>mortek@beispielpost.de</span>
  </div>
</section>

<section class="banner banner--en">
  <div class="banner__backdrop" role="img" aria-label="Dunkler Hintergrund mit weichen diagonalen Lichtstreifen"></div>
  <div class="brand">
    <div class="brand__square"></div>
    <div class="brand__block">
      <span class="brand__qualifier">MEISTERBETRIEB &amp; INGENIEURBÜRO</span>
      <span class="brand__name">mortek</span>
    </div>
  </div>
  <h2 class="headline">BUILDING WITH PASSION</h2>
  <p class="services">NEUBAU – UMBAU – ANBAU</p>
  <p class="address">Lindmoosweg 7, 89079 Ulm</p>
  <div class="contacts">
    <span class="contact"><svg class="contact__icon"><use href="#icon-phone"/></svg>+49 (0) 7305 - 4418273</span>
    <span class="contact"><svg class="contact__icon"><use href="#icon-mobile"/></svg>+49 (0) 176 - 20394857</span>
    <span class="contact"><svg class="contact__icon"><use href="#icon-mail"/></svg>mortek@beispielpost.de</span>
  </div>
</section>

</body>
</html>
```